Microsoft Word Template for 1, 2, and 4-page quick hit, topical pieces

I am looking for someone to create a professional and dynamic Microsoft Word Template that will allow us to easily add content to produce brochures and whitepapers on various topics. We'd like the template to be 4 pages with the idea that we may use all or just 1-2 of the pages in a brochure. We are fond of bold color, white space, and a good ratio of text to graphics. We have a large catalog of stock images so placeholders for photographs can be included if it fits the design. There is the possibility of expanded design opportunities in the future. I have attached our logo and colors.

Target Market(s)

Libraries - Public, Government, Higher Education, and Corporate

Font styles to use
Serif
Sans Serif

Requirements
Must have
• Editable Word Template that has 4 variable but cohesively designed pages. Use our logo and colors (see uploaded documents)
Nice to have
• Lots of white space, spaces for photos and graphics, spaces for blocks of text. Color.
Should not have
• Giant blocks of text. The exact same frame (header and footer) on each page.

```html
<!DOCTYPE html>
<html lang="en">
<head>
<meta charset="utf-8">
<title>Veridana brochure template pages</title>
<link rel="stylesheet" href="https://fonts.googleapis.com/css2?family=Karla:wght@400;600;700&display=swap">
<style>
  :root {
    --canvas: #f1f2f5;
    --paper: #ffffff;
    --teal: #0e7889;
    --gold: #f2a900;
    --olive: #98a80c;
    --orange: #e06a00;
    --maroon: #94001f;
    --ink: #4b4f4f;
    --brand: #9a5a12;
    --placeholder: #9b9b9b;
    --shot: #e4e7e8;
  }
  * { box-sizing: border-box; margin: 0; padding: 0; }
  html, body { width: 1200px; height: 900px; overflow: hidden; }
  body {
    background: var(--canvas);
    font-family: "Karla", Arial, sans-serif;
    position: relative;
  }
  .page {
    position: absolute;
    width: 334px;
    height: 463px;
    background: var(--paper);
    box-shadow: 0 8px 22px rgba(0,0,0,.16);
    overflow: hidden;
  }
  .page--cover { left: 72px; top: 71px; z-index: 1; }
  .page--story { left: 305px; top: 398px; z-index: 2; }
  .page--products { left: 546px; top: 59px; z-index: 3; }
  .page--back { left: 798px; top: 398px; z-index: 4; }

  .band { position: absolute; left: 0; width: 334px; }
  .band--orange { background: var(--orange); top: 393px; height: 70px; }
  .band--olive { background: var(--olive); top: 428px; height: 35px; }
  .band--teal { background: var(--teal); top: 438px; height: 25px; }
  .band--maroon { background: var(--maroon); top: 410px; height: 53px; }

  .header-art {
    position: absolute;
    left: 0; top: 0;
    width: 334px; height: 118px;
    background: linear-gradient(170deg, var(--teal) 0%, var(--teal) 45%, var(--gold) 70%, var(--olive) 100%);
  }

  .brand {
    position: absolute;
    display: flex;
    align-items: center;
    gap: 5px;
    color: var(--brand);
    font-weight: 400;
    letter-spacing: -0.2px;
    line-height: 1;
  }
  .brand__mark { border-radius: 50%; background: var(--gold); display: block; }
  .brand--large { font-size: 28px; }
  .brand--large .brand__mark { width: 26px; height: 26px; }
  .brand--small { font-size: 16px; }
  .brand--small .brand__mark { width: 14px; height: 14px; }

  .rule { position: absolute; height: 3px; background: var(--maroon); }
  .dots { position: absolute; display: flex; gap: 5px; }
  .dots span { width: 2.5px; height: 2.5px; border-radius: 50%; background: var(--maroon); }
  .dots--light span { background: #fff; }

  .copy {
    position: absolute;
    color: var(--ink);
    font-weight: 600;
    font-size: 10.6px;
    line-height: 13.6px;
    letter-spacing: 0.1px;
  }
  .copy .line { display: block; white-space: nowrap; }
  .copy p + p { margin-top: 13.6px; }
  .copy--cover { font-size: 10.3px; line-height: 12.8px; }

  .portrait {
    position: absolute;
    left: 231px; top: 114px;
    width: 81px; height: 81px;
    border-radius: 50%;
    background: radial-gradient(circle at 40% 40%, #d9c7ae, #5d6a72 70%, #2e3a44);
  }
  .image-slot {
    position: absolute;
    left: 29px; top: 138px;
    width: 264px; height: 119px;
    border-radius: 4px;
    background: var(--placeholder);
    color: #e9e9e9;
    font-size: 24px;
    font-weight: 400;
    display: flex; align-items: center; justify-content: center;
  }
  .screens {
    position: absolute;
    left: 0; top: 283px;
    width: 334px; height: 145px;
    background: linear-gradient(180deg, var(--shot), #f4f5f5 60%, #dfe3e4);
  }
  .web-link {
    position: absolute;
    left: 113px; top: 438px;
    color: #fff;
    font-size: 7.5px;
    font-weight: 700;
  }
</style>
</head>
<body>

<!-- Page 1: cover -->
<section class="page page--cover">
  <div class="header-art" role="img" aria-label="Decorative flowing colour ribbons in teal, gold and olive"></div>
  <div class="brand brand--large" style="left:29px; top:147px;"><span class="brand__mark"></span>veridana</div>
  <div class="portrait" role="img" aria-label="Photo of a smiling library staff member working at a computer"></div>
  <div class="rule" style="left:-3px; top:191px; width:150px;"></div>
  <div class="dots" style="left:155px; top:191px;"><span></span><span></span><span></span></div>
  <div class="copy copy--cover" style="left:29px; top:213px;">
    <p>
      <span class="line">Do you operate a service that provides information in</span>
      <span class="line">response to requests?&nbsp; Are you a Library, Gallery,</span>
      <span class="line">Museum, Archive, Knowledge Management team,</span>
      <span class="line">Business Data Research team or any other</span>
      <span class="line">organization that specializes in provision of</span>
      <span class="line">information in response to requests?&nbsp; Whether you</span>
      <span class="line">call it Reference Request Management, Library</span>
      <span class="line">Request Management, Research Request</span>
      <span class="line">Management, or even Information Request</span>
      <span class="line">Management, we do exactly what you need.</span>
    </p>
  </div>
  <div class="band band--orange"></div>
</section>

<!-- Page 3: story -->
<section class="page page--story">
  <div class="brand brand--small" style="left:29px; top:22px;"><span class="brand__mark"></span>veridana</div>
  <div class="dots" style="left:175px; top:31px;"><span></span><span></span><span></span></div>
  <div class="rule" style="left:208px; top:30px; width:126px;"></div>
  <div class="copy" style="left:29px; top:52px;">
    <p>
      <span class="line">Veridana has nearly 20 year's experience helping</span>
      <span class="line">information organizations like you to run their</span>
      <span class="line">request answering services more efficiently, while</span>
      <span class="line">generating statistics that validate the importance and</span>
      <span class="line">value of the service you provide.</span>
    </p>
    <p>
      <span class="line">We are specialists in the request answering</span>
      <span class="line">functions of your information service and we</span>
      <span class="line">recognize the importance of those services to your</span>
      <span class="line">organization's reputation today, and into the future.</span>
      <span class="line">Our vision means we partner with you to provide</span>
      <span class="line">more reasons for end users to seek out and use your</span>
      <span class="line">services, to provide responses more efficiently, and</span>
      <span class="line">to measure the impact of the work required to</span>
      <span class="line">provide those services as the volume of</span>
      <span class="line">electronically available information increases.</span>
    </p>
  </div>
  <div class="screens" role="img" aria-label="Screenshots of the request tracking and statistics software"></div>
  <div class="band band--olive"></div>
</section>

<!-- Page 2: products -->
<section class="page page--products">
  <div class="brand brand--small" style="left:29px; top:23px;"><span class="brand__mark"></span>veridana</div>
  <div class="dots" style="left:178px; top:31px;"><span></span><span></span><span></span></div>
  <div class="rule" style="left:211px; top:30px; width:123px;"></div>
  <div class="copy" style="left:29px; top:86px;">
    <p>
      <span class="line">We understand the importance of your request</span>
      <span class="line">answering functions to the future of your information</span>
      <span class="line">delivery service.</span>
    </p>
  </div>
  <div class="image-slot">Image</div>
  <div class="copy" style="left:29px; top:274px;">
    <p>
      <span class="line">Veridana's web based products are specifically</span>
      <span class="line">designed to help information delivery organizations</span>
      <span class="line">manage the intake, assignment and response</span>
      <span class="line">development for each request, as well as enable the</span>
      <span class="line">construction of a more useful, reusable, work</span>
      <span class="line">product.&nbsp; Responses can be delivered in the most</span>
      <span class="line">efficient ways no matter what the size or</span>
      <span class="line">requirements of your organization and no matter</span>
      <span class="line">what communication methods or other tools you use.</span>
      <span class="line">And detailed statistics are generated just from doing</span>
      <span class="line">that work.</span>
    </p>
  </div>
  <div class="band band--teal"></div>
</section>

<!-- Page 4: back cover -->
<section class="page page--back">
  <div class="band band--maroon"></div>
  <div class="brand brand--small" style="left:181px; top:390px;"><span class="brand__mark"></span>veridana</div>
  <div class="rule" style="left:0; top:443px; width:87px; height:1.5px; background:#fff;"></div>
  <div class="dots dots--light" style="left:92px; top:442px;"><span></span><span></span><span></span></div>
  <div class="web-link">https://www.veridana.com/Home.aspx</div>
</section>

</body>
</html>
```